Bottle labels and logo for small distillery

Marsh Hollow Distillery is a small beginning project of handcrafted distillery producing cider spirit (same as apple wine spirit) and apple vodka from apple wine. There are not many similar small distilleries in the Baltic Sea region and very few of them produce apple brandy, so the concept and the product itself are unique. That is the reason we are not developing any distinctive brand and we are sticking to two elements – company name ‘Marsh Hollow Distillery OÜ’ and product name ‘Orchardveil’. Best branding solution for us would be to have a clear logo instead of words.

In the future it is most likely that the product range will broaden by some type of sweet liqueurs like apple-liqueur and black-currant-liqueur and both will be mixtures of natural juice and apple brandy.

We have tested the product itself and more or less chosen proper bottle and closing. Example of the shape of the bottle:

https://www.vessel-depot-example.co.uk/Containers/Containers/500ml-containers/500ml-clear-container-Brevo.html

Sizes of bottles:
500 ml Height (without cap) 350 mm, external diameter 60 mm;
375 ml Height (without cap) 330 mm, external diameeter 55 mm;

The bottle cap/closing is going to be waxed, and should look something like that:

http://img.picvault-example.com/qT7Rz.jpg

The design has two separate parts: (1) paper bottle label and (2) print on the bottle.

Front side – printed to the bottle, preferably a symbol without text, for better quality of print rather a vector graphics (monochrome or up to 3-single colour picture). We would like to use the symbol also as an enterprise logo if possible (but logo and bottle print can also be different if designer decides so). It should give a hint to apple based distillate (but, we do not want to narrow down creators fantasy so if you have a good idea please don’t hold back). Just to offer a dumb examples:
https://moodloft-example.com/entry/51830962
https://www.snapboard-example.ca/pin/917263540812355019/?lp=true https://www.stockvista-example.com/image-vector/decorative-apple-flora-ornaments-leaf-flower-208473615?src=QXR_kpLwVb8TyR3HxM_42q-2-50
NB! these are just examples of style, contents are more or less random.

Back side – a rectangular shaped label glued to the bottle. Label should not be a square but rather oblong and narrow. The colour of the label shouldn’t be white but rather light yellow, light brown or light creamy. Some examples:

https://www.snapboard-example.co.uk/pin/720954183627104958 https://www.snapboard-example.co.uk/pin/839172046558213940

Label has to contain such information:
1) (Product in large print) Orchardveil
2) (product) apple wine spirit
3) (Neto amount) 50 cl; / 35 cl
4) (Ethanol in large print) 45%; / 55%
5) (Producer) Produced by Marsh Hollow Distillery, Harjumaa 74211, Paldiski, Lõhmuse 9;
6) (raw material and technology) Made in Estonia. Product is made of Estonian apple wine and distilled in reflux still in small batches
7) (distillate) Distillate 85%
8) (batch no) Batch no: (stamp) …
9) (note) produced with utmost pleasure
10) (note) Consume responsibly
11) (signature) distiller: …

We also need the label to be designed in Estonian as follows:
1) Orchardveil
2) Õunaveini destillaat
3) 50 cl; / 35 cl
4) 45% / 55%
5) Toodetud Marsh Hollow Distillery OÜ poolt, Harjumaal 74211, Paldiski, Lõhmuse 9;
6) Toodetud Eestis, eestimaisest õunaveinist ja destilleeritud käsitööna väikeste partiidena
7) Destillaat 85%
8) Partii nr:
9) Toodetud puhtast rõõmust
10) Tarbige vastutustundlikult!
11) Meister:

Design as such can be the same. Since we are planning to bottle the product in 375 ml and 500 ml bottles and dilute it down to 45% and 55%. So, there should be 37,5 cl 45%, 50 cl 45%; 37,5 cl 55%; 50 cl 55%.

We assume that in case of 37,5 cl and 50 cl bottles we can use the same design and just resize the printed image and paper-label a bit.

Since the product is handmade and high quality we would like to stress credibility. Not as important as the first purchase is the second purchase of clients – the label should not be shocking but rather trustworthy. And classy in the very best sense.

We are hoping to have a long term business relationship with possible future designer.

Target Market(s)

Adult male alcohol consumers

Industry/Entity Type

Food Production

Logo Text

Marsh Hollow Distillery

Colors

Designer to choose colors to be used in the design.

```html
<!DOCTYPE html>
<html lang="en">
<head>
<meta charset="utf-8">
<title>Orchardveil – Marsh Hollow Distillery labels</title>
<link rel="stylesheet" href="https://fonts.googleapis.com/css2?family=Rammetto+One&family=Arimo:wght@400;700&family=Cardo:wght@700&display=swap">
<style>
  :root {
    --paper: #ffffff;
    --label-cream: #fefcd2;
    --label-frame: #9a5a30;
    --brand-red: #8e0f12;
    --apple-red: #b3231c;
    --ink: #222222;
    --ink-soft: #3a3a3a;
  }
  * { margin: 0; padding: 0; box-sizing: border-box; }
  html, body { width: 1129px; height: 1200px; overflow: hidden; background: var(--paper); }
  .canvas { position: relative; width: 1129px; height: 1200px; background: var(--paper); font-family: "Arimo", Arial, sans-serif; color: var(--ink); }

  .brand-mark { position: absolute; left: 28px; top: 40px; width: 330px; text-align: center; }
  .brand-mark .mark-circle { display: block; width: 290px; height: 290px; margin: 0 auto 36px; border-radius: 50%; background: var(--apple-red); }
  .brand-mark .brand-name { font-family: "Rammetto One", sans-serif; font-size: 40px; color: var(--brand-red); line-height: 1; }

  .label { position: absolute; background: var(--label-cream); border-radius: 34px; padding: 8px; text-align: center; }
  .label-frame { width: 100%; height: 100%; border: 2px solid var(--label-frame); border-radius: 28px; display: flex; flex-direction: column; align-items: center; padding: 12px 6px; }

  .label-dot { border-radius: 50%; background: var(--apple-red); flex: none; }
  .product-name { font-family: "Rammetto One", sans-serif; color: var(--brand-red); line-height: 1.1; }
  .spirit-title { font-family: "Rammetto One", sans-serif; color: var(--brand-red); line-height: 1.15; }
  .producer-serif { font-family: "Cardo", serif; font-weight: 700; color: var(--ink-soft); line-height: 1.15; }

  .info .kind { font-weight: 700; font-size: 11px; margin-top: 6px; }
  .info .volume { font-size: 11px; margin-top: 10px; }
  .info .ethanol-label { font-size: 14px; margin-top: 10px; color: var(--ink-soft); }
  .info .ethanol { font-size: 25px; line-height: 1.1; color: var(--ink-soft); }
  .info .tiny { font-size: 7px; line-height: 1.25; }
  .info .small-bold { font-size: 10px; font-weight: 700; line-height: 1.15; }
  .info .mid { font-size: 9px; line-height: 1.25; }
  .info .sign { align-self: flex-start; padding-left: 14px; font-size: 10px; margin-top: 8px; }

  .label-en-small { left: 356px; top: 566px; width: 146px; height: 365px; }
  .label-en-front { left: 531px; top: 566px; width: 144px; height: 365px; }
  .label-en-large { left: 740px; top: 536px; width: 158px; height: 406px; }
  .label-et-large { left: 936px; top: 534px; width: 160px; height: 408px; }
</style>
</head>
<body>
<main class="canvas">

  <section class="brand-mark">
    <span class="mark-circle"></span>
    <div class="brand-name">Orchardveil</div>
  </section>

  <article class="label label-en-small info">
    <div class="label-frame">
      <span class="label-dot" style="width:40px;height:40px;"></span>
      <div class="product-name" style="font-size:9px;margin-top:6px;">Orchardveil</div>
      <div class="kind">Apple Wine Spirit</div>
      <div class="volume">35 cl</div>
      <div class="ethanol-label">Ethanol :</div>
      <div class="ethanol">45%/55%</div>
      <div class="tiny" style="margin-top:6px;">Produced by:</div>
      <div class="small-bold">Marsh Hollow Distillery,</div>
      <div class="tiny">Harjumaa 74211, Paldiski, Lõhmuse 9</div>
      <div class="small-bold" style="margin-top:5px;">Made in Estonia.</div>
      <div class="tiny">Product is made of<br>Estonian apple wine and<br>distilled in reflux still<br>in small batches</div>
      <div class="small-bold" style="margin-top:3px;">Destillate 85%</div>
      <div class="mid" style="margin-top:10px;">Batch no: ..................</div>
      <div class="tiny">Produce with utmost pleasure<br>Consume responsibly</div>
      <div class="sign">Distiller:</div>
    </div>
  </article>

  <article class="label label-en-front">
    <div class="label-frame">
      <span class="label-dot" style="width:80px;height:80px;margin-top:20px;"></span>
      <div class="product-name" style="font-size:15px;margin-top:18px;">Orchardveil</div>
      <div class="spirit-title" style="font-size:25px;margin-top:26px;">Apple<br>Wine<br>Spirit</div>
      <div style="font-size:11px;margin-top:auto;">Produced by:</div>
      <div class="producer-serif" style="font-size:13px;margin-bottom:10px;">Marsh Hollow Distillery</div>
    </div>
  </article>

  <article class="label label-en-large">
    <div class="label-frame">
      <span class="label-dot" style="width:100px;height:100px;margin-top:16px;"></span>
      <div class="product-name" style="font-size:17px;margin-top:16px;">Orchardveil</div>
      <div class="spirit-title" style="font-size:28px;margin-top:22px;">Apple<br>Wine<br>Spirit</div>
      <div style="font-size:12px;margin-top:auto;">Produced by:</div>
      <div class="producer-serif" style="font-size:14px;margin-bottom:10px;">Marsh Hollow Distillery</div>
    </div>
  </article>

  <article class="label label-et-large info">
    <div class="label-frame">
      <span class="label-dot" style="width:54px;height:54px;"></span>
      <div class="product-name" style="font-size:11px;margin-top:8px;">Orchardveil</div>
      <div class="kind" style="margin-top:4px;">Õunaveini destillaat</div>
      <div class="volume">50 cl</div>
      <div class="ethanol-label" style="font-size:15px;">Ethanol :</div>
      <div class="ethanol" style="font-size:27px;">45%/55%</div>
      <div class="tiny" style="margin-top:8px;">Toodetud</div>
      <div class="small-bold">Marsh Hollow Distillery OÜ poolt,</div>
      <div class="tiny">Harjumaal 74211, Paldiski, Lõhmuse 9</div>
      <div class="mid" style="margin-top:10px;">Toodetud Eestis,eestimaisest õunaveinist ja destilleeritud käsitööna väikeste partiidena</div>
      <div class="small-bold" style="margin-top:2px;">Destillaat 85%</div>
      <div class="mid" style="margin-top:12px;">Partii nr: ..................</div>
      <div class="tiny">Toodetud puhtast roomust<br>Tarbige vastututstundlikult!</div>
      <div class="sign" style="font-size:11px;">Meister:</div>
    </div>
  </article>

</main>
</body>
</html>
```